Stillpoint Coach website development

Need a website designed for a coaching business. Very high-end, luxury, professionalism, in the area of STRESS, see brief attached. I have a logo already
Updates

Slow in providing feedback

Target Market(s)

CEOs very successful men and wealthy females, high end luxury market

Industry/Entity Type

coaching

Number of Pages Required

1 page

Requirements
Must have
• Luxury look, professional, serious but warm, appealing to both sexes

```html
<!DOCTYPE html>
<html lang="en">
<head>
<meta charset="utf-8">
<title>Stillpoint Coach</title>
<link rel="stylesheet" href="https://fonts.googleapis.com/css2?family=Figtree:wght@400;600;700;800&display=swap">
<style>
  :root {
    --ink: #3e6c85;
    --ink-soft: #5f7f92;
    --muted: #8a8f96;
    --paper: #f4f7fb;
    --white: #ffffff;
    --footer: #426f87;
    --stage: #eef1f5;
  }
  * { box-sizing: border-box; margin: 0; padding: 0; }
  html, body { width: 1200px; height: 1200px; overflow: hidden; }
  body {
    background: var(--stage);
    font-family: "Figtree", Arial, sans-serif;
    color: var(--ink);
    position: relative;
  }
  .page {
    position: absolute;
    left: 328px;
    top: 5px;
    width: 800px;
    height: 1750px;
    transform: scale(0.68);
    transform-origin: 0 0;
    background: var(--white);
    box-shadow: 0 20px 60px rgba(60, 80, 100, 0.12);
    overflow: hidden;
  }

  /* Navigation */
  .site-nav {
    height: 68px;
    background: var(--paper);
    display: flex;
    align-items: center;
    justify-content: center;
    gap: 30px;
  }
  .site-nav a, .footer-nav a {
    text-decoration: none;
    color: var(--ink);
    font-size: 8.5px;
    letter-spacing: 2px;
    text-transform: uppercase;
  }
  .brand {
    display: flex;
    flex-direction: column;
    align-items: center;
    gap: 6px;
    margin: 0 24px;
    color: var(--ink);
    font-size: 8.5px;
    font-weight: 700;
    letter-spacing: 3px;
    text-transform: uppercase;
  }
  .brand-square { width: 12px; height: 12px; background: currentColor; }

  /* Hero */
  .hero {
    position: relative;
    height: 355px;
    background: linear-gradient(100deg, #5a3a2a 0%, #8a6a58 30%, #c9bcb0 48%, #7a5240 62%, #2a2526 78%, #4a3328 100%);
  }
  .hero h1 {
    position: absolute;
    left: 65px;
    top: 154px;
    color: var(--white);
    font-size: 30px;
    font-weight: 800;
    line-height: 40px;
    letter-spacing: -0.5px;
  }

  /* Welcome */
  .welcome {
    height: 224px;
    background: var(--paper);
    text-align: center;
    padding-top: 40px;
  }
  .section-title {
    font-size: 25px;
    font-weight: 600;
    color: var(--ink);
    letter-spacing: -0.3px;
  }
  .welcome p {
    width: 335px;
    margin: 6px auto 0;
    font-size: 8.5px;
    line-height: 13.4px;
    color: var(--ink);
  }

  /* Quote band */
  .quote-band {
    position: relative;
    height: 302px;
    background: linear-gradient(90deg, #e4e3e0 0%, #e8e7e5 50%, #dcdcd8 62%, #6f9a6a 75%, #3f7d45 88%, #9a9a96 100%);
  }
  .quote-band p {
    position: absolute;
    left: 52px;
    top: 66px;
    width: 380px;
    color: var(--white);
    font-size: 30px;
    font-weight: 800;
    line-height: 40px;
    letter-spacing: -0.4px;
  }

  /* Benefits */
  .benefits {
    height: 393px;
    text-align: center;
    padding-top: 38px;
    background: var(--white);
  }
  .benefit-grid {
    display: grid;
    grid-template-columns: repeat(3, 230px);
    justify-content: center;
    row-gap: 24px;
    margin-top: 22px;
  }
  .benefit svg { width: 34px; height: 34px; display: block; margin: 0 auto; }
  .benefit h3 {
    margin-top: 12px;
    font-size: 15px;
    font-weight: 600;
    color: var(--ink);
  }
  .benefit p {
    width: 180px;
    margin: 6px auto 0;
    font-size: 8px;
    line-height: 13px;
    color: var(--muted);
  }

  /* Stress impact */
  .impact {
    position: relative;
    height: 280px;
    background: var(--paper);
  }
  .impact-photo {
    position: absolute;
    left: 56px;
    top: -27px;
    width: 324px;
    height: 229px;
    background: radial-gradient(circle at 25% 35%, #e6e6e6 0%, #b8b8b8 40%, #9a9a9a 70%, #c8c8c8 100%);
  }
  .impact-copy {
    position: absolute;
    left: 410px;
    top: 45px;
    width: 335px;
  }
  .impact-copy h2 { font-size: 24px; font-weight: 600; letter-spacing: -0.3px; }
  .impact-copy p {
    margin-top: 14px;
    font-size: 8.5px;
    line-height: 13.4px;
    color: var(--ink);
  }

  /* Footer */
  .site-footer {
    height: 128px;
    background: var(--footer);
    color: var(--white);
    text-align: center;
    padding-top: 26px;
  }
  .site-footer .brand { color: var(--white); }
  .footer-nav {
    display: flex;
    justify-content: center;
    gap: 12px;
    margin-top: 16px;
  }
  .footer-nav a { color: #d6e3ea; }
  .copyright {
    margin-top: 16px;
    font-size: 7.5px;
    color: #c2d4de;
  }
</style>
</head>
<body>
<div class="page">
  <nav class="site-nav">
    <a href="#">Stress</a>
    <a href="#">Method</a>
    <div class="brand"><span class="brand-square"></span>Stillpoint Coach</div>
    <a href="#">About</a>
    <a href="#">Contact</a>
  </nav>

  <header class="hero" role="img" aria-label="Photo of a smiling man in a dark suit standing in a brick-walled city alley">
    <h1>Help people lead a better<br>and healthier life.</h1>
  </header>

  <section class="welcome">
    <h2 class="section-title">Welcome to StillpointCoach</h2>
    <p>Stillpoint Coach came about due to my desire to help people lead a better and healthier life. Initially, I was involved in the fitness/body side of health. As years passed and my experience grew, I realized how important the mind was in total wellness, and that the mind is all powerful and controlling. Control the mind, control the body and achieve success. Stress can be the most debilitating factor in our lives, it is the root cause of so many diseases and costs the US workplace an estimated 300 billion dollars due to loss of productivity.</p>
  </section>

  <section class="quote-band" role="img" aria-label="Photo of a green succulent plant in a concrete pot against a pale grey wall">
    <p>Control the mind, control the body and achieve success.</p>
  </section>

  <section class="benefits">
    <h2 class="section-title">Benefits</h2>
    <div class="benefit-grid">
      <div class="benefit">
        <svg viewBox="0 0 34 34" fill="none" stroke="#9bb6c6" stroke-width="1"><rect x="7" y="5" width="20" height="24"/><circle cx="13" cy="14" r="3"/><path d="M9 22c1-3 7-3 8 0M19 12h6M19 15h6M19 18h4"/></svg>
        <h3>Experience</h3>
        <p>Lorem ipsum dolor sit amet, consectetur adipiscing elit. Sed erat nibh tristique ipsum.</p>
      </div>
      <div class="benefit">
        <svg viewBox="0 0 34 34" fill="none" stroke="#9bb6c6" stroke-width="1"><path d="M8 3h13l5 5v22H8z"/><path d="M12 12h10M12 16h8M12 20h5"/><circle cx="24" cy="23" r="3"/><path d="M19 31c1-3 9-3 10 0"/></svg>
        <h3>Sector Expert</h3>
        <p>Lorem ipsum dolor sit amet, consectetur adipiscing elit. Sed erat nibh tristique ipsum.</p>
      </div>
      <div class="benefit">
        <svg viewBox="0 0 34 34" fill="none" stroke="#9bb6c6" stroke-width="1"><rect x="6" y="5" width="22" height="24" rx="3"/><circle cx="17" cy="15" r="5"/><path d="M17 20v5"/></svg>
        <h3>Excellent Listener</h3>
        <p>Lorem ipsum dolor sit amet, consectetur adipiscing elit. Sed erat nibh tristique ipsum.</p>
      </div>
      <div class="benefit">
        <svg viewBox="0 0 34 34" fill="none" stroke="#9bb6c6" stroke-width="1"><circle cx="17" cy="11" r="6"/><path d="M5 31c1-8 23-8 24 0z"/><path d="M17 22v8"/></svg>
        <h3>Industry professionals</h3>
        <p>Lorem ipsum dolor sit amet, consectetur adipiscing elit. Sed erat nibh tristique ipsum.</p>
      </div>
      <div class="benefit">
        <svg viewBox="0 0 34 34" fill="none" stroke="#9bb6c6" stroke-width="1"><circle cx="17" cy="17" r="13"/><rect x="12" y="16" width="10" height="8"/><path d="M14 16v-3a3 3 0 0 1 6 0v3"/></svg>
        <h3>Confidentiality</h3>
        <p>Lorem ipsum dolor sit amet, consectetur adipiscing elit. Sed erat nibh tristique ipsum.</p>
      </div>
      <div class="benefit">
        <svg viewBox="0 0 34 34" fill="none" stroke="#9bb6c6" stroke-width="1"><path d="M28 14a12 12 0 1 0-2 11"/><path d="M28 8v6h-6"/><circle cx="17" cy="16" r="5"/></svg>
        <h3>Other</h3>
        <p>Lorem ipsum dolor sit amet, consectetur adipiscing elit. Sed erat nibh tristique ipsum.</p>
      </div>
    </div>
  </section>

  <section class="impact">
    <div class="impact-photo" role="img" aria-label="Black and white close-up photo of a twisted, weathered branch"></div>
    <div class="impact-copy">
      <h2>How is stress impacting you?</h2>
      <p>Stress is not all bad, and since we are surrounded by engulfed by stress, or it isn't going anywhere soon, we need to deal with it, and even better, channel to be an advantage/tool to perform better.<br>Recognize when we are feeling stress and what is causing it, understand it, and how we react to it is the first step. Then when we sense it's coming we can deal with it, resolve it, or use it to our advantage</p>
    </div>
  </section>

  <footer class="site-footer">
    <div class="brand"><span class="brand-square"></span>Stillpoint Coach</div>
    <nav class="footer-nav">
      <a href="#">Stress</a>
      <a href="#">Method</a>
      <a href="#">About</a>
      <a href="#">Contact</a>
    </nav>
    <p class="copyright">© 2022 STILLPOINT COACH. All rights reserved</p>
  </footer>
</div>
</body>
</html>
```